Velmar Industrial Coatings

We are looking to improve our business cards. Our company installs industrial floor and wall coatings in industrial, chemical and food processing plants.
Our coatings which consist of epoxy, urethane, and vinyl esters provide chemical and abrasion resistant surface with non-skid properties that are easy to clean.

Target Market(s)

food manufacturing, chemical plants, breweries and wineries, warehouses, clean room floors.

Industry/Entity Type

Construction

Contact Information for Business Card

improved current logo.

Colors

Designer to choose colors to be used in the design.

Requirements
Must have
• the information from uploaded file
Nice to have
• "We'll be outstanding on your floors."

```html
<!DOCTYPE html>
<html lang="en">
<head>
<meta charset="utf-8">
<title>Velmar Industrial Coatings – Business Card</title>
<link rel="stylesheet" href="https://fonts.googleapis.com/css2?family=Montserrat:wght@400;500;700&display=swap">
<style>
  :root {
    --backdrop: #3a2f2a;
    --paper: #f4f4f2;
    --olive: #4f5a2c;
    --olive-deep: #3d4622;
    --lime: #a9c93b;
    --ink: #1c1c1c;
    --ink-soft: #2b2b2b;
  }
  html, body {
    margin: 0;
    width: 1200px;
    height: 716px;
    overflow: hidden;
    background: var(--backdrop);
    font-family: "Montserrat", sans-serif;
  }
  .stage {
    position: relative;
    width: 1200px;
    height: 716px;
  }
  .card {
    position: absolute;
    top: 204px;
    width: 540px;
    height: 309px;
    overflow: hidden;
    box-shadow: 0 14px 30px rgba(0,0,0,.45);
  }
  .card--front { left: 40px; background: var(--paper); }
  .card--back { left: 620px; background: var(--olive); }

  .card__decor { position: absolute; inset: 0; }

  .holder-name {
    position: absolute;
    left: 36px;
    top: 52px;
    margin: 0;
    font-size: 16px;
    font-weight: 700;
    letter-spacing: .5px;
    color: var(--olive);
  }
  .contact-list {
    position: absolute;
    left: 36px;
    top: 100px;
    margin: 0;
    padding: 0;
    list-style: none;
    font-size: 12.5px;
    line-height: 19px;
    color: var(--ink-soft);
  }
  .contact-list li { display: flex; align-items: center; gap: 7px; }
  .contact-list svg { width: 10px; height: 10px; fill: var(--olive); flex: none; }

  .brand {
    position: absolute;
    display: flex;
    align-items: center;
    gap: 8px;
    font-weight: 700;
    text-transform: uppercase;
  }
  .brand__square { flex: none; }
  .brand--front {
    right: 30px;
    top: 58px;
    font-size: 12px;
    color: var(--ink);
  }
  .brand--front .brand__square { width: 14px; height: 14px; background: var(--olive); }
  .brand--back {
    left: 0; right: 0;
    top: 0; bottom: 0;
    justify-content: center;
    font-size: 24px;
    letter-spacing: .5px;
    color: var(--lime);
  }
  .brand--back .brand__square { width: 26px; height: 26px; background: var(--lime); }

  .address {
    position: absolute;
    right: 40px;
    top: 212px;
    margin: 0;
    font-style: normal;
    text-align: right;
    font-size: 12.5px;
    line-height: 17px;
    color: var(--ink-soft);
  }
  .website {
    position: absolute;
    right: 40px;
    bottom: 7px;
    font-size: 12.5px;
    color: #ffffff;
  }
</style>
</head>
<body>
<main class="stage">

  <section class="card card--front" aria-label="Business card front">
    <svg class="card__decor" viewBox="0 0 540 309" aria-hidden="true">
      <line x1="30" y1="80" x2="300" y2="80" stroke="#1c1c1c" stroke-width="1.4"/>
      <line x1="250" y1="196" x2="510" y2="196" stroke="#1c1c1c" stroke-width="1.4"/>
      <rect x="0" y="262" width="250" height="4" fill="#1c1c1c"/>
      <path d="M0 270 H235 Q245 270 250 279 Q254 282 262 282 H540 V309 H0 Z" fill="#4f5a2c"/>
      <path d="M0 270 H235 Q245 270 250 279 L236 276 H0 Z" fill="#1c1c1c"/>
    </svg>

    <h1 class="holder-name">REID CALLOWAY</h1>

    <ul class="contact-list">
      <li><svg viewBox="0 0 10 10"><path d="M2 0l2 2.5-1 1.2a6 6 0 0 0 3.3 3.3l1.2-1L10 8 8.5 10C4 9.5.5 6 0 1.5z"/></svg>1-800-555-0142</li>
      <li><svg viewBox="0 0 10 10"><path d="M2 0l2 2.5-1 1.2a6 6 0 0 0 3.3 3.3l1.2-1L10 8 8.5 10C4 9.5.5 6 0 1.5z"/></svg>(360) 555-0131</li>
      <li><svg viewBox="0 0 10 10"><path d="M2 0h6v3h2v7H0V3h2zM3 1v2h4V1zM2 5v1h2V5zm4 0v1h2V5z"/></svg>(360) 555-0133</li>
      <li><svg viewBox="0 0 10 10"><path d="M2.5 0h5v10h-5zM3.5 1v7h3V1z"/></svg>(360) 555-0176</li>
      <li><svg viewBox="0 0 10 10"><path d="M0 2h10v6H0zm1 .8L5 5.6 9 2.8z"/></svg>reid@velmarfloors.com</li>
    </ul>

    <div class="brand brand--front">
      <span class="brand__square"></span>
      <span class="brand__name">Velmar Industrial Coatings Inc.</span>
    </div>

    <address class="address">
      Velmar Inc<br>
      Po Box 412<br>
      Cedar Bend, Wa 98000
    </address>

    <span class="website">www.velmarfloors.com</span>
  </section>

  <section class="card card--back" aria-label="Business card back">
    <div class="brand brand--back">
      <span class="brand__square"></span>
      <span class="brand__name">Velmar Industrial Coatings Inc.</span>
    </div>
  </section>

</main>
</body>
</html>
```